2026 Varnex Loprin LWB Vehicle Wrap Design for Ridgeway Electrical and Refrigeration Work Vans

We are Ridgeway Electrical and Refrigeration — a Perth-based commercial electrical, air conditioning and refrigeration company. We service commercial buildings, homes and luxury residential jobs across the metro area and remote WA.
We need a clean, professional and high-impact full vehicle wrap design for our work vans. The vans are our mobile billboards, so the design needs to look sharp from a distance, communicate trust and competence, and clearly show what we do.
Must include:

Our company name: Ridgeway Electrical and Refrigeration
Tagline options (you can choose the strongest placement or suggest alternatives):
“Electrical | Air Conditioning | Refrigeration – Perth & Remote WA”
Licence numbers "AU051237 and EC24813"
Phone number: 0491 538 214
Website: ridgewayelectricalrefrigeration.com.au
Email: admin@ridgewayelectricalrefrigeration.com.au
Our existing logo (will be uploaded)

Style we want:

Professional, modern and trustworthy
Bold enough to stand out on the road but not flashy or overly busy
Clean hierarchy so the company name and phone number are readable at speed
Strong use of contrast

Colour preferences:

Prefer designs that work with our existing branding (we will upload the logo and brand colours)
Open to strong, professional colour combinations (navy/dark blue, black, white, and one accent colour such as orange, red or electric blue often work well in the trades)

Avoid:

Cluttered designs with too much text
Cartoonish or overly “tradie” looking graphics
Designs that look cheap or dated

Additional notes:

Design should scale well so we can use the same concept across multiple vans
We will need print-ready files (high-res, layered) at the end

Please upload your best concepts. We will give clear feedback and work with the winning designer to refine the final artwork for production.

Target Market(s)

commercial buildings, homes and luxury residential jobs across the metro area and remote WA.

Industry/Entity Type

Electrical, Air Conditioning and Refrigeration

Colors
0054AA
0677BA
7BADD7
CADEEF
E8F1F8

Requirements
Must have
• Our company name: Ridgeway Electrical and Refrigeration Tagline options (you can choose the strongest placement or suggest alternatives): “Electrical | Air Conditioning | Refrigeration – Perth & Remote WA” Licence numbers "AU051237 and EC24813" Phone number: 0491 538 214 Website: ridgewayelectricalrefrigeration.com.au Email: admin@ridgewayelectricalrefrigeration.com.au Our existing logo (will be uploaded)
Nice to have
• Professional, modern and trustworthy Bold enough to stand out on the road but not flashy or overly busy Clean hierarchy so the company name and phone number are readable at speed Strong use of contrast
Should not have
• Cluttered designs with too much text Cartoonish or overly “tradie” looking graphics Designs that look cheap or dated

```html
<!DOCTYPE html>
<html lang="en">
<head>
<meta charset="utf-8">
<title>Ridgeway Electrical and Refrigeration – Van Wrap Side Panel</title>
<link rel="stylesheet" href="https://fonts.googleapis.com/css2?family=Poppins:ital,wght@0,500;0,600;0,700;0,800;1,800&display=swap">
<style>
  :root {
    --brand-blue: #0a63d2;
    --deep-blue: #0054aa;
    --brand-red: #ec1c24;
    --mid-purple: #6b4585;
    --white: #ffffff;
    --page: #ffffff;
  }
  html, body {
    margin: 0;
    padding: 0;
    width: 1057px;
    height: 1200px;
    overflow: hidden;
    background: var(--page);
  }
  .canvas {
    position: relative;
    width: 1057px;
    height: 1200px;
  }
  .wrap-panel {
    position: absolute;
    left: 38px;
    top: 387px;
    width: 980px;
    height: 425px;
  }
  .wrap-panel text { font-family: "Poppins", sans-serif; }
  .service-line { font-weight: 800; font-style: italic; font-size: 62px; fill: var(--white); letter-spacing: -1px; }
  .region-line { font-weight: 800; font-style: italic; font-size: 58px; fill: var(--brand-red); letter-spacing: -1px; }
  .brand-name { font-weight: 700; fill: var(--brand-blue); }
  .licence-label { font-weight: 600; font-size: 15px; fill: var(--white); }
  .licence-number { font-weight: 600; font-size: 21px; fill: var(--white); }
  .phone-number { font-weight: 700; font-size: 58px; fill: var(--white); letter-spacing: -1px; }
  .contact-line { font-weight: 600; font-size: 23px; fill: var(--white); }
</style>
</head>
<body>
<main class="canvas">
  <svg class="wrap-panel" viewBox="0 0 1640 712" role="img" aria-label="Ridgeway Electrical and Refrigeration van side wrap layout">
    <defs>
      <linearGradient id="bodyGradient" x1="0" y1="0" x2="1" y2="0">
        <stop offset="0" stop-color="var(--brand-blue)"/>
        <stop offset="0.38" stop-color="var(--brand-blue)"/>
        <stop offset="0.58" stop-color="var(--mid-purple)"/>
        <stop offset="0.8" stop-color="var(--brand-red)"/>
        <stop offset="1" stop-color="var(--brand-red)"/>
      </linearGradient>
      <linearGradient id="phoneGradient" x1="0" y1="0" x2="1" y2="0">
        <stop offset="0" stop-color="var(--brand-blue)"/>
        <stop offset="0.2" stop-color="var(--brand-blue)"/>
        <stop offset="0.55" stop-color="var(--mid-purple)"/>
        <stop offset="0.85" stop-color="var(--brand-red)"/>
      </linearGradient>
    </defs>

    <!-- base body shape -->
    <path class="body-shape" d="M0,424 L331,52 Q370,0 451,0 L1640,0 L1640,712 L0,712 Z" fill="url(#bodyGradient)"/>

    <!-- service stripes -->
    <g class="service-stripes">
      <path d="M1002,8 H1640 V112 H1002 A52,52 0 0 1 1002,8 Z" fill="var(--brand-red)"/>
      <path d="M820,62 H1574 A52,52 0 0 1 1574,166 H820 Z" fill="var(--brand-blue)"/>
      <path d="M846,118 H1590 V222 H846 A52,52 0 0 1 846,118 Z" fill="var(--brand-red)"/>
      <path d="M900,172 H1574 A52,52 0 0 1 1574,276 H900 Z" fill="var(--brand-blue)"/>
      <rect x="1560" y="0" width="80" height="56" fill="var(--brand-blue)"/>
      <rect x="993" y="57" width="600" height="5" fill="var(--mid-purple)"/>
      <rect x="840" y="168" width="740" height="5" fill="var(--mid-purple)"/>
      <rect x="1180" y="222" width="400" height="5" fill="var(--mid-purple)"/>
      <text class="service-line" x="1561" y="114" text-anchor="end">ELECTRICAL</text>
      <text class="service-line" x="1561" y="169" text-anchor="end">AIR CONDITIONING</text>
      <text class="service-line" x="1561" y="224" text-anchor="end">REFRIGERATION</text>
    </g>

    <!-- white information field -->
    <path class="info-field" d="M391,282 H1640 V657 H391 A187.5,187.5 0 0 1 391,282 Z" fill="var(--white)"/>
    <text class="region-line" x="1561" y="375" text-anchor="end">PERTH &amp; REMOTE WA</text>

    <!-- company name block -->
    <g class="brand-block">
      <rect x="346" y="386" width="60" height="60" fill="var(--brand-blue)"/>
      <text class="brand-name" x="346" y="492" font-size="34">RIDGEWAY</text>
      <text class="brand-name" x="346" y="524" font-size="22">ELECTRICAL &amp;</text>
      <text class="brand-name" x="346" y="550" font-size="22">REFRIGERATION</text>
    </g>

    <!-- phone band -->
    <path class="phone-band" d="M712,419 H1530 A110,110 0 0 1 1640,529 V657 H712 A119,119 0 0 1 712,419 Z" fill="url(#phoneGradient)"/>
    <rect class="phone-pill" x="726" y="495" width="835" height="95" rx="47.5" fill="var(--brand-blue)"/>
    <text class="licence-label" x="736" y="524">Licence numbers</text>
    <text class="licence-number" x="736" y="550">AU051237</text>
    <text class="licence-number" x="736" y="575">EC24813</text>
    <text class="phone-number" x="885" y="566">0491 538 214</text>

    <!-- web and email -->
    <g class="contact-row">
      <circle cx="268" cy="684" r="11" fill="none" stroke="var(--white)" stroke-width="2.5"/>
      <line x1="257" y1="684" x2="279" y2="684" stroke="var(--white)" stroke-width="2"/>
      <text class="contact-line" x="290" y="692">ridgewayelectricalrefrigeration.com.au</text>
      <rect x="830" y="668" width="2" height="32" fill="var(--white)"/>
      <rect x="846" y="674" width="26" height="19" rx="4" fill="none" stroke="var(--white)" stroke-width="2.5"/>
      <polyline points="850,679 859,686 868,679" fill="none" stroke="var(--white)" stroke-width="2.5"/>
      <text class="contact-line" x="882" y="692">admin@ridgewayelectricalrefrigeration.com.au</text>
    </g>
  </svg>
</main>
</body>
</html>
```